Norwegian psychologist service needs a fresh and exiting web site*

Norwegian psychologist service: working with therapy, personal development, mastery and personal growth. Focus: children and teenagers with special needs; family dynamics; group processes; individuals with a need for therapy and personal growth. (Our company name: Kildeløft og ro (means Mastery and Growth).

We already have a logo for the company, which will be used (will be attached in the project).

The webside is to be structured in 4 pages with roll down curtain menus (the numbers are just for guiding the designer - the should not be added):

Page 1: Om Kildeløft og Ro (about Mastery and Growth): this is where our business is is presented/described shortly: Lorem Ipsum dolor cit...

Page 2: Tjenester (Services): this is where our 5 service areas are presented:
2.1 Utredning (Investigation, diagnosing): Lorem Ipsum dolor cit...
2.2 Rådgivning (consulting): Lorem Ipsum dolor cit...

2.3 Kurs og work shops (courses and work shops): Lorem Ipsum dolor cit...
2.3a Kildeløft og ro Tema 1 (T1)
2.3b Kildeløft og ro Tema 2 (T2)
2.3c Kildeløft og ro Tema 3 (T3)

2.4 Terapi og utvikling (Therapy and development)
2.4a Kildeløft og ro for individer (KR1)
2.4b Kildeløft og ro i familier (KR2)
2.4c Kildeløft og ro i grupper (KR3)
2.4d Kildeløft og ro i institusjoner (KR4)

Page 3: Aktuelt (Blog): this is our blog where we share knowledge and articles

Page 4: Kontakt (Contact): This is the contact form page. Contact form should constitute:
- Ditt navn (your name)
- E-post (your e-mail)
- Emne (subject)
- Melding (message/description)

Our project should also include suggestion for handheld units (iPhone, iPad).
Updates

We have both been traveling with work for a while, and then unfortunately both of us got sick on return, so we need a few more days to evaluate and choose design. Kind Regards Arne & Ragnhild

Target Market(s)

Focus on therapy, learning, mastery and growth for children and teenagers with special needs, within the family dynamics, or in a group setting.
OUR MARKETS:
Private market: individuals, families, groups and health industry institutions (with focus on learning, mastery, growth (as well as growing up) and psychiatry for children and teenagers with special difficulties and needs)
Public institutions: Government institutions, state institutions and municipality institutions (e.g. schools, municipality health service, hospitals) that serve the public (families with children and teenagers with special needs, and where learning, mastery, growth (as well as growing up) and potential psychiatry is an issue).

Number of Pages Required

4 page

Font styles to use
Sans Serif

Colors

Designer to choose colors to be used in the design.

Requirements
Must have
• The website must have 4 pages with roll down curtain menus (we have added a PDF with suggested structure, and headings, with sub menus - see attached PDF drawing.
• The web page must also use the added logo file - and make the web page work well with our logo.
• We would like the website to have a modern look and we would like the site to be associated with typical HIGH END TOP QUALITY private health institutions, but with a stronger focus on human beings (hands, faces etc), and not white coats and doctors. We are psychologists in the private market.
• For instance, if photos are being used - we tend to like "warm" almost art-like, "grainy" two-tone (e.g. sepia) photos to illustrate our focus. If designer can find such photos as part of design, it would be interesting to us. We would like a few photos like that integrated in the design.
• We also want a design suggestion for how the web page should look like and behave on handheld units (e.g. iPhone, iPad).
Nice to have
• If designer could find a number of suitable photos that matches the business idea and design requirements (see description above), that could follow website, that would be good.
• It could also be nice to have graphic symbols that denote the different pages/subpages (subjects)....
• HORSES: we sometimes use horses as a "tool" in therapy sessions. The horse is not necessarily used for riding, but for contact, communication and grooming. PHOTOS: we would like the designer to find an opportunity for using a photo reflecting this cooperation between therapist, child, teenager and horse. It is a bit up to the designer to find a way to do this... Since the horse is only a tool, among many other tools, it does not have to be much - but we want to try and see how it will work with a photo that also reflects this part of our business.

```html
<!DOCTYPE html>
<html lang="no">
<head>
<meta charset="utf-8">
<title>Kildeløft og Ro</title>
<link href="https://fonts.googleapis.com/css2?family=Roboto:wght@400;500;700;900&display=swap" rel="stylesheet">
<style>
:root{
  --brand:#2b3990;
  --brand-dark:#232f7d;
  --ink:#1f1f1f;
  --ink-soft:#333;
  --white:#fff;
  --rule:#d6d6d6;
}
*{box-sizing:border-box;margin:0;padding:0}
html,body{width:1200px;height:3195px;overflow:hidden;background:var(--white)}
body{position:relative;font-family:'Roboto',Arial,sans-serif;color:var(--ink)}
.abs{position:absolute}

/* top bar */
.topbar{top:0;left:0;width:1200px;height:58px;background:var(--brand);color:var(--white)}
.info{display:flex;align-items:center;gap:8px;top:12px;font-size:11px;font-weight:500;line-height:14px}
.info .ico{width:34px;height:34px;border-radius:50%;background:var(--white);display:flex;align-items:center;justify-content:center}
.info .txt{border-left:1px solid var(--white);padding-left:6px}
.info b{font-weight:700;display:block}
.social-top{top:13px;left:921px;display:flex;gap:9px}
.social-top span{width:32px;height:32px;border-radius:50%;background:var(--white);display:block}

/* hero */
.hero{top:58px;left:0;width:1200px;height:615px;background:linear-gradient(100deg,#7a7fb5 0%,#6f76b0 35%,#5d67a8 60%,#8a8ec0 100%)}
.logo{top:72px;left:84px;display:flex;align-items:center;gap:6px;color:var(--white);font-size:15px;font-weight:500}
.logo i{width:14px;height:14px;border-radius:50%;background:var(--white);display:block}
.nav{top:91px;left:0;width:1200px;font-size:14px;font-weight:700;color:var(--white)}
.nav a{position:absolute;color:inherit;text-decoration:none}
.hero-title{top:248px;width:1200px;text-align:center;color:var(--white);font-size:44px;font-weight:900;line-height:54px}
.hero-text{top:380px;left:220px;width:760px;text-align:center;color:var(--white);font-size:14px;font-weight:700;line-height:18.5px}
.btn-light{top:485px;left:505px;width:190px;height:41px;border-radius:4px;background:var(--white);color:var(--brand);font-size:14px;font-weight:500;display:flex;align-items:center;justify-content:center}

/* sections */
.section-title{width:1200px;text-align:center;font-size:37px;font-weight:700}
.rule{height:4px;background:var(--brand)}
.intro{top:766px;left:312px;width:576px;text-align:center;font-size:14px;font-weight:500;line-height:18px}

.photo{display:block}
.feature h3{position:absolute;font-size:40px;font-weight:500;color:var(--brand)}
.feature .lead{position:absolute;width:460px;font-size:14.5px;color:var(--brand);line-height:18px;font-weight:500}
.feature .body{position:absolute;width:465px;font-size:13.5px;line-height:17px;color:var(--ink)}
.feature .right{text-align:right}
.btn-small{position:absolute;width:88px;height:29px;border-radius:4px;background:var(--brand);color:var(--white);font-size:12px;font-weight:700;display:flex;align-items:center;justify-content:center;gap:5px;box-shadow:0 2px 4px rgba(0,0,0,.35)}
.overlay-cta{left:600px;top:1100px;width:512px;text-align:center;color:var(--white);font-size:32px;font-weight:700;letter-spacing:1px}

.divider{top:2456px;left:0;width:1200px;height:1px;background:var(--rule)}
.quote{top:2580px;left:305px;width:568px;text-align:center;font-size:16px;line-height:20px;color:var(--ink-soft)}
.qmark{font-size:64px;font-weight:900;font-style:italic;color:var(--brand);line-height:1}
.avatar{border-radius:50%;border:2px solid var(--brand);background:linear-gradient(160deg,#9a9a9a,#4a4a4a)}
.person{top:2823px;width:1200px;left:0;text-align:center;font-size:18px;font-weight:500;color:var(--brand)}

/* footer */
.footer{top:2881px;left:0;width:1200px;height:314px;background:var(--brand);border-top:3px solid #e6e6e6;color:var(--white)}
.col-title{position:absolute;top:2906px;font-size:17px;font-weight:700}
.col-rule{position:absolute;top:2940px;height:2px;background:var(--white)}
.flink{position:absolute;font-size:15.5px;font-weight:500;display:flex;align-items:center;gap:6px}
.flink i{width:22px;height:22px;border-radius:50%;background:var(--white);display:block}
.signup{top:2995px;left:619px;width:233px;height:26px;border:1px solid var(--white);border-radius:4px;font-size:10px;color:#c9cdea;padding:6px 10px}
.copyright{top:3158px;left:0;width:1200px;text-align:center;font-size:15px;font-weight:500;color:var(--white)}
</style>
</head>
<body>

<header class="abs topbar">
  <div class="abs info" style="left:87px">
    <span class="ico"><svg width="20" height="20" viewBox="0 0 20 20"><circle cx="10" cy="10" r="8" fill="none" stroke="#2b3990" stroke-width="1.8"/><path d="M10 5v5l3 2" fill="none" stroke="#2b3990" stroke-width="1.8"/></svg></span>
    <span class="txt">OUR SCHEDULE<b>8:00am - 5:00pm</b></span>
  </div>
  <div class="abs info" style="left:338px">
    <span class="ico"><svg width="20" height="16" viewBox="0 0 20 16"><rect x="1.5" y="2" width="17" height="12" rx="1.5" fill="none" stroke="#2b3990" stroke-width="1.6"/><path d="M2 3l8 6 8-6" fill="none" stroke="#2b3990" stroke-width="1.6"/></svg></span>
    <span class="txt">EMAIL ADDRESS<b>post@kildeloftogro.no</b></span>
  </div>
  <div class="abs info" style="left:655px">
    <span class="ico"><svg width="18" height="18" viewBox="0 0 24 24"><path d="M6.6 10.8a15 15 0 0 0 6.6 6.6l2.2-2.2c.3-.3.7-.4 1-.2 1.1.4 2.3.6 3.6.6.6 0 1 .4 1 1V20c0 .6-.4 1-1 1A17 17 0 0 1 3 4c0-.6.4-1 1-1h3.5c.6 0 1 .4 1 1 0 1.3.2 2.5.6 3.6.1.3 0 .7-.2 1z" fill="#2b3990"/></svg></span>
    <span class="txt">OUR PHONE NUMBER<b>555.010.2290</b></span>
  </div>
  <div class="abs social-top"><span></span><span></span><span></span><span></span><span></span></div>
</header>

<section class="abs hero" role="img" aria-label="Photo of a therapist sitting with a young boy in a playroom, tinted blue"></section>
<div class="abs logo"><i></i>Kildeløft og ro</div>
<nav class="abs nav">
  <a style="left:540px">OM KILDELØFT OG RO</a>
  <a style="left:777px">TJENESTER</a>
  <a style="left:921px">AKTUELT</a>
  <a style="left:1046px">KONTAKT</a>
</nav>
<h1 class="abs hero-title">WELCOM TO<br>KILDELØFT OG RO</h1>
<p class="abs hero-text">Lorem ipsum dolor sit amet, consetetur sadipscing elitr, sed diam nonumy eirmod tempor invidunt ut labore et dolore magna aliquyam erat, sed diam voluptua.<br>At vero eos et accusam et justo duo dolores et ea rebum. Stet clita kasd gubergren, no sea takimata sanctus est Lorem ipsum dolor sit</p>
<div class="abs btn-light">Learn More</div>

<h2 class="abs section-title" style="top:692px;color:var(--brand)">What We Do?</h2>
<div class="abs rule" style="top:748px;left:514px;width:170px"></div>
<p class="abs intro">Lorem ipsum dolor sit amet, consetetur sadipscing elitr, sed diam nonumy eirmod tempor invidunt ut labore et dolore magna aliquyam erat, sed diam voluptua. At vero eos et accusam et justo duo dolores et ea rebum.</p>

<!-- feature 1 -->
<section class="feature">
  <h3 style="left:87px;top:960px">Lorem Ipsum</h3>
  <div class="abs rule" style="top:1021px;left:87px;width:170px"></div>
  <p class="lead" style="left:87px;top:1040px">Lorem ipsum dolor sit amet, consetetur sadipscing elitr, sed diam nonumy eirmod tempor invidunt ut labore.</p>
  <p class="body" style="left:87px;top:1093px">Et dolore magna aliquyam erat, sed diam voluptua. At vero eos et accusam et justo duo dolores et ea rebum.<br>Stet clita kasd gubergren, no sea takimata sanctus est Lorem ipsum dolor sit amet. Lorem ipsum dolor sit amet, consetetur sadipscing elitr, sed diam nonumy eirmod tempor invidunt ut labore et dolore magna aliquyam erat, sed diam voluptua. At vero eos et accusam et justo duo dolores et ea rebum. Stet clita kasd gubergren, no sea takimata sanctus est Lorem ipsum dolor sit amet.</p>
  <div class="btn-small" style="left:87px;top:1243px">Learn More <svg width="6" height="7"><path d="M0 0l6 3.5L0 7z" fill="#fff"/></svg></div>
  <div class="abs photo" style="left:600px;top:864px;width:512px;height:511px;background:linear-gradient(135deg,#8f95c8,#6e76b4 50%,#5a64a6)" role="img" aria-label="Photo of a family sitting together on a sofa in a counselling session, tinted blue"></div>
  <div class="abs overlay-cta">Learn More</div>
</section>

<!-- feature 2 -->
<section class="feature">
  <div class="abs photo" style="left:87px;top:1376px;width:513px;height:512px;background:linear-gradient(160deg,#e9e6e1,#d8d2c8 50%,#b49a7c)" role="img" aria-label="Photo of a little girl playing with a wooden toy horse on the floor"></div>
  <h3 class="right" style="left:700px;width:412px;top:1472px">Lorem Ipsum</h3>
  <div class="abs rule" style="top:1533px;left:952px;width:170px"></div>
  <p class="lead right" style="left:662px;top:1552px">Lorem ipsum dolor sit amet, consetetur sadipscing elitr, sed diam nonumy eirmod tempor invidunt ut labore.</p>
  <p class="body right" style="left:657px;top:1605px">Et dolore magna aliquyam erat, sed diam voluptua. At vero eos et accusam et justo duo dolores et ea rebum.<br>Stet clita kasd gubergren, no sea takimata sanctus est Lorem ipsum dolor sit amet. Lorem ipsum dolor sit amet, consetetur sadipscing elitr, sed diam nonumy eirmod tempor invidunt ut labore et dolore magna aliquyam erat, sed diam voluptua. At vero eos et accusam et justo duo dolores et ea rebum. Stet clita kasd gubergren, no sea takimata sanctus est Lorem ipsum dolor sit amet.</p>
  <div class="btn-small" style="left:1034px;top:1754px">Learn More <svg width="6" height="7"><path d="M0 0l6 3.5L0 7z" fill="#fff"/></svg></div>
</section>

<!-- feature 3 -->
<section class="feature">
  <h3 style="left:87px;top:1987px">Lorem Ipsum</h3>
  <div class="abs rule" style="top:2048px;left:87px;width:170px"></div>
  <p class="lead" style="left:87px;top:2067px">Lorem ipsum dolor sit amet, consetetur sadipscing elitr, sed diam nonumy eirmod tempor invidunt ut labore.</p>
  <p class="body" style="left:87px;top:2120px">Et dolore magna aliquyam erat, sed diam voluptua. At vero eos et accusam et justo duo dolores et ea rebum.<br>Stet clita kasd gubergren, no sea takimata sanctus est Lorem ipsum dolor sit amet. Lorem ipsum dolor sit amet, consetetur sadipscing elitr, sed diam nonumy eirmod tempor invidunt ut labore et dolore magna aliquyam erat, sed diam voluptua. At vero eos et accusam et justo duo dolores et ea rebum. Stet clita kasd gubergren, no sea takimata sanctus est Lorem ipsum dolor sit amet.</p>
  <div class="btn-small" style="left:87px;top:2270px">Learn More <svg width="6" height="7"><path d="M0 0l6 3.5L0 7z" fill="#fff"/></svg></div>
  <div class="abs photo" style="left:600px;top:1888px;width:512px;height:512px;background:linear-gradient(150deg,#5a3a2c,#b08a6a 45%,#e8e2d8)" role="img" aria-label="Photo of a mother and son painting eggs at a table"></div>
</section>

<div class="abs divider"></div>

<h2 class="abs section-title" style="top:2492px;left:-12px;color:var(--ink-soft)">Testimonials</h2>
<div class="abs rule" style="top:2548px;left:503px;width:170px"></div>
<div class="abs qmark" style="left:281px;top:2552px">“</div>
<p class="abs quote">Lorem ipsum dolor sit amet, consetetur sadipscing elitr, sed diam nonumy eirmod tempor invidunt ut labore et dolore magna aliquyam erat, sed diam voluptua. At vero eos et accusam et justo duo dolores et ea rebum.<br>Stet clita kasd gubergren, no sea takimata sanctus est Lorem ipsum dolor sit amet. Lorem ipsum dolor sit amet, consetetur sadipscing elitr, sed diam</p>
<div class="abs qmark" style="left:877px;top:2654px">”</div>

<div class="abs avatar" style="left:353px;top:2713px;width:78px;height:78px" role="img" aria-label="Client portrait"></div>
<div class="abs avatar" style="left:444px;top:2713px;width:78px;height:78px" role="img" aria-label="Client portrait"></div>
<div class="abs avatar" style="left:536px;top:2694px;width:116px;height:116px" role="img" aria-label="Portrait of Jonas Berg"></div>
<div class="abs avatar" style="left:665px;top:2713px;width:78px;height:78px" role="img" aria-label="Client portrait"></div>
<div class="abs avatar" style="left:756px;top:2713px;width:78px;height:78px" role="img" aria-label="Client portrait"></div>
<div class="abs person">Jonas Berg</div>

<footer class="abs footer"></footer>
<div class="col-title" style="left:86px">COMPANY</div>
<div class="col-rule" style="left:86px;width:88px"></div>
<div class="flink" style="left:87px;top:2960px;color:#fff">About</div>
<div class="flink" style="left:87px;top:3000px;color:#fff">Terms and Polices</div>
<div class="flink" style="left:87px;top:3040px;color:#fff">Guidelines</div>

<div class="col-title" style="left:378px;color:#fff">SUPPORT</div>
<div class="col-rule" style="left:378px;width:84px"></div>
<div class="flink" style="left:378px;top:2960px;color:#fff">Contact</div>
<div class="flink" style="left:378px;top:3000px;color:#fff">Terms of us</div>

<div class="col-title" style="left:619px;color:#fff">NEWSLETTER</div>
<div class="col-rule" style="left:619px;width:117px"></div>
<div class="flink" style="left:619px;top:2960px;color:#fff">Join our monthly newsletter</div>
<div class="abs signup">John@......
  <svg class="abs" style="right:8px;top:5px" width="20" height="14" viewBox="0 0 20 14"><rect x="1" y="1" width="18" height="12" rx="1" fill="none" stroke="#fff" stroke-width="1.4"/><path d="M1.5 2l8.5 6 8.5-6" fill="none" stroke="#fff" stroke-width="1.4"/></svg>
</div>

<div class="col-title" style="left:1008px;color:#fff">Follow us</div>
<div class="col-rule" style="left:1008px;width:80px"></div>
<div class="flink" style="left:1008px;top:2959px;color:#fff"><i></i>Fjordbok</div>
<div class="flink" style="left:1008px;top:2999px;color:#fff"><i></i>Bildestrøm</div>
<div class="flink" style="left:1008px;top:3039px;color:#fff"><i></i>Nettverket</div>
<div class="flink" style="left:1008px;top:3079px;color:#fff"><i></i>Kvitter</div>
<div class="flink" style="left:1008px;top:3119px;color:#fff"><i></i>Filmkanal</div>

<div class="abs copyright">All rights reserved @KILDELØFT OG RO</div>

</body>
</html>
```